VEXO requires an exciting new business card

New business card required for VEXO. We are a new market research consultancy and want our brand to be approachable and be contemporary/modern, bold, uncomplicated/simple, and use friendly and easy to read fonts.

A draft website front page is attached to give you a feel (the pictures will be improved over the coming days).

The business card will be printed on 600gsm card, full colour both sides. The card is unique in that it allows one of four colours to be placed within the seam of the card (see http://uk.tarnix.com/products/halo/business-cards.html)

The logo has been designed in yellow on white, white on yellow, yellow on black and black on yellow - please select whichever you feel most appropriate from the attached document (please use the versions with the tagline). I think my preference is yellow on white for the front, and then yellow or black as the dominant colour on the back.

Telephone numbers will be given next week as they are now being finalised.

Thanks

Target Market(s)

Professionals in large corporates, such as Marketing Managers at Bravik, Fizzor Dune, Domacore etc.

Industry/Entity Type

Market Research

Requirements
Must have
• Greg Hallow QPMR
vexo
Level 4, 17 Ember St
Quindle Park
NSW 2087
Tel: 02 XXXX XXXX
Mob: XXXX XXXXXX
Email: greg@vexomr.com.au
Web: www.vexomr.com.au

```html
<!DOCTYPE html>
<html lang="en">
<head>
<meta charset="utf-8">
<title>VEXO Business Card</title>
<link rel="stylesheet" href="https://fonts.googleapis.com/css2?family=Lexend:wght@400&display=swap">
<style>
  :root {
    --sheet: #d3d3d3;
    --brand-yellow: #ffcb05;
    --panel-white: #ffffff;
    --card-black: #000000;
    --edge-grey: #8a8a8a;
    --label-ink: #111111;
  }
  html, body {
    margin: 0;
    padding: 0;
    overflow: hidden;
  }
  body {
    width: 1200px;
    height: 1141px;
    background: var(--sheet);
    position: relative;
    font-family: "Lexend", sans-serif;
    font-weight: 400;
  }
  .card {
    position: absolute;
    left: 13px;
    width: 934px;
    box-sizing: border-box;
  }
  .card--front {
    top: 40px;
    height: 533px;
    background: var(--brand-yellow);
  }
  .card--back {
    top: 603px;
    height: 530px;
    background: var(--card-black);
    border: 3px solid var(--edge-grey);
  }
  .name-panel {
    position: absolute;
    top: 0;
    left: 139px;
    width: 661px;
    background: var(--panel-white);
    display: flex;
    align-items: center;
    justify-content: center;
  }
  .card--front .name-panel {
    height: 299px;
    border-radius: 0 0 30px 30px;
  }
  .card--back .name-panel {
    left: 136px;
    height: 165px;
    border-radius: 0 0 24px 24px;
  }
  .brand-name {
    color: var(--brand-yellow);
    line-height: 1;
  }
  .card--front .brand-name { font-size: 120px; }
  .card--back .brand-name { font-size: 80px; }
  .contact {
    position: absolute;
    left: 40px;
    top: 176px;
    margin: 0;
    color: var(--brand-yellow);
    font-size: 34px;
    line-height: 41px;
    font-style: normal;
  }
  .contact p { margin: 0; white-space: nowrap; }
  .side-label {
    position: absolute;
    left: 982px;
    margin: 0;
    color: var(--label-ink);
    font-size: 40px;
    line-height: 52px;
  }
  .side-label--front { top: 188px; }
  .side-label--back { top: 858px; }
</style>
</head>
<body>
  <section class="card card--front" aria-label="Card front">
    <div class="name-panel">
      <span class="brand-name">vexo</span>
    </div>
  </section>
  <p class="side-label side-label--front">Front<br>side</p>

  <section class="card card--back" aria-label="Card back">
    <div class="name-panel">
      <span class="brand-name">vexo</span>
    </div>
    <address class="contact">
      <p>Greg Hallow QPMR vexo</p>
      <p>Level 4, 17 Ember St</p>
      <p>Quindle Park</p>
      <p>NSW 2087</p>
      <p>Tel: 02 XXXX XXXX</p>
      <p>Mob: XXXX XXXXXX</p>
      <p>Email: greg@vexomr.com.au</p>
      <p>Web: www.vexomr.com.au</p>
    </address>
  </section>
  <p class="side-label side-label--back">Back<br>Side</p>
</body>
</html>
```